New Stationary Design

Harcourt Electrics Ltd have acquired Brockhurst Catering Equipment Ltd. We will be retaining the Brockhurst Catering Equipment Ltd name and require new letter head, compliment slips & business card designs.

I have attached the existing Harcourt Electrics letterhead to show our current image/brand. I do not wish to change this substantially & imagine maybe a swap of colours from Red logo to Blue, and the title & footer bars maybe in Red. That said, I'm open to subtle changes in the overall design & to maybe modernise it and if we like them, we would probably ask the Designer to update the changes to reflect them on the Harcourt Electrics stationary as well.

We will be able to get some proper high def images for Catering equipment to include, but for the time being if desingers can use any standard stock images for initial presentation.

The logo will be printed onto a Red van so somehow we need to be able to modify it for that use.

Brockhurst Catering Equipment Ltd. Correspondence Address: 47 Lower Fenwick Road, Northampton. NN3 8QS. Tel 01604 738 902. Fax 01604 738 417. No website currently. Registered No: 05817264. Vat No: 481 3306 59. Company Registered Address: 22 Maplin Crescent, Leicester. LE2 7RD. We would also like to mention that we have Regional Service Centres also based in Leicester & Stockport.

Business Cards would be for;

Owen Hartley, Director. owen.hartley@brockhurstcatering-example.co.uk

Steven Pelham, Operations Manager. steven.pelham@brockhurstcatering-example.co.uk

Neil Booth, Service Manager. neil.booth@brockhurstcatering-example.co.uk

Martin Rowley, Business Development Manager. martin.rowley@brockhurstcatering-example.co.uk

We would also like the letter head to include the 'Fuel Guard' logo & our registration Number: To be confirmed. Also the Electrical Contractors logo & the words Wiring Installers Federation underneath so people know what it means. See www.wif-example.co.uk

Target Market(s)

Businesses who use Catering Equipment such as Cookers. fridges etc. Hence, Care Homes, Hospitals, Restaurants etc

Industry/Entity Type

Business

Requirements
Must have
• Resemblance to existing Harcourt Electrics brand, although maybe with some changes & modernisation.
Nice to have
• Could maybe have some 'icons' for the type of equipment we sell instead of photos. Ie Cookers, Ovens, Fridges, Microwaves, Dishwashers, as well as kithen cateringtabling, commercial extraction hoods etc.

```html
<!DOCTYPE html>
<html lang="en">
<head>
<meta charset="utf-8">
<title>Brockhurst Catering Equipment Ltd. Letterhead</title>
<link href="https://fonts.googleapis.com/css2?family=Arimo:wght@400;700&display=swap" rel="stylesheet">
<style>
  :root {
    --brand-red: #e3202a;
    --brand-navy: #1d3f8f;
    --paper: #ffffff;
    --badge-yellow: #f4d418;
    --badge-blue: #7aa6cf;
    --footer-text: #ffffff;
  }
  * { margin: 0; padding: 0; box-sizing: border-box; }
  html, body { width: 850px; height: 1200px; overflow: hidden; background: var(--paper); }
  body { font-family: "Arimo", Arial, sans-serif; }
  .letterhead { position: relative; width: 850px; height: 1200px; background: var(--paper); overflow: hidden; }

  .title-bar { position: absolute; top: 0; left: 0; width: 100%; height: 100px; background: var(--brand-red); }

  .brand-mark {
    position: absolute; top: 17px; left: 25px; width: 208px; height: 115px;
    background: var(--brand-navy); border: 3px solid var(--paper);
    outline: 3px solid var(--brand-navy);
    display: flex; align-items: center; gap: 12px; padding: 0 14px;
  }
  .brand-mark__square { flex: 0 0 20px; height: 20px; background: var(--paper); }
  .brand-mark__name {
    font-weight: 700; font-size: 21px; line-height: 1.12; letter-spacing: 0.2px;
    color: var(--paper); text-transform: uppercase;
  }

  .equipment-image {
    position: absolute; left: 0; top: 965px; width: 345px; height: 235px;
    background: linear-gradient(180deg, #e8ecef 0%, #c9d0d6 55%, #9aa3ab 100%);
  }

  .footer-bar { position: absolute; left: 0; bottom: 0; width: 100%; height: 98px; background: var(--brand-red); }
  .footer-details {
    position: absolute; left: 350px; top: 1108px; color: var(--footer-text);
    font-size: 9.5px; line-height: 15px; white-space: nowrap;
  }
  .footer-details .company { opacity: 0.8; }
  .footer-details strong { font-weight: 700; }

  .accreditation { position: absolute; }
  .accreditation--fuel { left: 606px; top: 1008px; width: 58px; height: 82px; background: var(--badge-yellow); }
  .accreditation--wiring { left: 684px; top: 1018px; width: 104px; height: 56px; background: var(--badge-blue); opacity: 0.6; }
</style>
</head>
<body>
<div class="letterhead">
  <header class="title-bar"></header>
  <div class="brand-mark">
    <span class="brand-mark__square"></span>
    <span class="brand-mark__name">Brockhurst Catering Equipment Ltd.</span>
  </div>

  <div class="equipment-image" role="img" aria-label="Catering appliances: fridge freezer, oven, microwave and dishwasher"></div>

  <div class="accreditation accreditation--fuel" role="img" aria-label="Fuel Guard registration badge"></div>
  <div class="accreditation accreditation--wiring" role="img" aria-label="Wiring Installers Federation membership badge"></div>

  <footer class="footer-bar"></footer>
  <div class="footer-details">
    <p class="company">Brockhurst Catering Equipment Ltd</p>
    <p><strong>Head office:</strong>&nbsp;&nbsp; 47 Lower Fenwick Road, Northampton. NN3 8QS · Tel 01604 738 902 · Fax 01604 738 417</p>
    <p><strong>Registered Address:</strong> 22 Maplin Crescent, Leicester. LE2 7RD</p>
    <p><strong>Regional Service Centres also based in Leicester &amp; Stockport</strong></p>
    <p><strong>Registered No: 05817264 · Vat No: 481 3306 59</strong></p>
  </div>
</div>
</body>
</html>
```